Lanterne architecture business cards

We are a new company based in New Zealand. We Specialize in High end Luxury Residential Architecture.

Every home is bespoke and is designed to each clients individual requirements and needs.

I like to design buildings that inspire people through light and form while offering a high level of comfort and usability.

Lines of sight, proportion and balance are fundamental to the spaces I create.
Updates

August 5th is current deadline - Today's date is the 13th of August.

Target Market(s)

New Zealanders who want a custom individual home design, typically 30-65 year old males and females

Industry/Entity Type

Architecture

Contact Information for Business Card

Director - Derek Tolson
Contact Number - 0279164073
Email - info@lanternearchitecture-example.co.nz
Webstie - www.lanternearchitecture-example.co.nz
Social Media - @lanternearchitecture

Font styles to use
Sans Serif

Requirements
Must have
• Logo (Both Sides)
Website
Email
Contact Number
Social Media

Nice to have
• Texture
Should not have
• More than 3 colours - typically I would've thought 2 would be good to match the logo.

```html
<!DOCTYPE html>
<html lang="en">
<head>
<meta charset="utf-8">
<title>Lanterne Architecture – Business Cards</title>
<link rel="stylesheet" href="https://fonts.googleapis.com/css2?family=Jost:wght@300;400;500&family=Source+Sans+3:wght@400&display=swap">
<style>
  :root {
    --backdrop: #e7efee;
    --paper: #ffffff;
    --ink: #000000;
    --gold: #cfc36e;
  }
  * { margin: 0; padding: 0; box-sizing: border-box; }
  html, body {
    width: 1200px;
    height: 1200px;
    overflow: hidden;
    background: var(--backdrop);
  }
  .sheet {
    position: relative;
    width: 1200px;
    height: 1200px;
  }
  .card {
    position: absolute;
    left: 249px;
    width: 679px;
    height: 388px;
  }
  .card--front { top: 186px; background: var(--paper); }
  .card--back  { top: 626px; background: var(--ink); }

  /* Front */
  .front-brand {
    position: absolute;
    left: 24px;
    top: 52px;
    width: 250px;
    display: flex;
    flex-direction: column;
    align-items: center;
  }
  .brand-ring {
    width: 150px;
    height: 150px;
    border: 22px solid var(--gold);
    border-radius: 50%;
  }
  .front-brand .brand-name {
    margin-top: 26px;
    font-family: "Jost", sans-serif;
    font-weight: 400;
    font-size: 17px;
    letter-spacing: 0.22em;
    color: var(--gold);
    text-transform: uppercase;
    white-space: nowrap;
  }
  .divider {
    position: absolute;
    left: 292px;
    top: 43px;
    width: 2px;
    height: 297px;
    background: var(--gold);
  }
  .person {
    position: absolute;
    right: 48px;
    top: 40px;
    text-align: right;
    font-family: "Jost", sans-serif;
    color: var(--ink);
    text-transform: uppercase;
  }
  .person__name {
    font-weight: 400;
    font-size: 47px;
    line-height: 1;
    letter-spacing: 0.01em;
  }
  .person__role {
    margin-top: 6px;
    font-weight: 400;
    font-size: 26px;
    line-height: 1;
  }
  .contact {
    position: absolute;
    left: 336px;
    top: 218px;
    list-style: none;
    font-family: "Source Sans 3", sans-serif;
    font-size: 19.5px;
    line-height: 33px;
    color: var(--ink);
  }
  .contact__phone { font-family: "Jost", sans-serif; letter-spacing: 0.04em; }

  /* Back */
  .back-ring {
    position: absolute;
    left: 295px;
    top: 94px;
    width: 90px;
    height: 90px;
    border: 11px solid var(--gold);
    border-radius: 50%;
  }
  .back-brand {
    position: absolute;
    left: 0;
    right: 0;
    top: 236px;
    text-align: center;
    font-family: "Jost", sans-serif;
    font-weight: 300;
    color: var(--gold);
    text-transform: uppercase;
  }
  .back-brand__main {
    display: block;
    font-size: 43px;
    line-height: 1;
    letter-spacing: 0.62em;
    margin-right: -0.62em;
  }
  .back-brand__sub {
    display: block;
    margin-top: 14px;
    font-size: 13px;
    line-height: 1;
    letter-spacing: 2.75em;
    margin-right: -2.75em;
  }
</style>
</head>
<body>
<main class="sheet">
  <section class="card card--front" aria-label="Business card front">
    <div class="front-brand">
      <div class="brand-ring"></div>
      <span class="brand-name">Lanterne</span>
    </div>
    <div class="divider"></div>
    <div class="person">
      <h1 class="person__name">Derek Tolson</h1>
      <p class="person__role">Director</p>
    </div>
    <ul class="contact">
      <li class="contact__phone">0279164073</li>
      <li>info@lanternearchitecture-example.co.nz</li>
      <li>www.lanternearchitecture-example.co.nz</li>
      <li>@lanternearchitecture</li>
    </ul>
  </section>

  <section class="card card--back" aria-label="Business card back">
    <div class="back-ring"></div>
    <p class="back-brand">
      <span class="back-brand__main">Lanterne</span>
      <span class="back-brand__sub">Architecture</span>
    </p>
  </section>
</main>
</body>
</html>
```